Business Postcard Design for Personal Training Company

Need a postcard design for my company called "Cobalt Stride" Colors are Navy Blue, Blue, Grey and White.

On the front I want there to be pictures and it to feature a box that says "Free Consultation + 50% off your first session!"

And somehow to feature the following phrases " Lose Weight. Gain Muscle."
"Customized Personal training using V-Core, the latest technology in fitness. Reach your fitness goals in just two 25-min sessions per week"

Also want featured the following phrases (maybe on back):

"up to 18 times more effective than a conventional gym workout"

I need the back of the postcard to have all my business information:

Address: 327 Venadero Ave, Building B Suite 518, Costa Mesa CA 92626
Website: cobalt-stride.example
Phone #: (949) 555-0137
E-mail: cobaltstridehealth@mailbox.example

I am going to upload my logo, before and after pictures and pictures of people training on the device. Feel free to use as many/or little photos as you want.

Target Market(s)

Wealthy Adults 40+ years old looking for a personal trainer

Industry/Entity Type

Personal Trainer

Colors
0455a3
85cae6
aaaaaa
ffffff

Requirements
Must have
• At least two of the before and after photos, and two or more photos of people working out on the device.

```html
<!DOCTYPE html>
<html lang="en">
<head>
<meta charset="utf-8">
<title>Cobalt Stride Postcard</title>
<link href="https://fonts.googleapis.com/css2?family=Roboto+Condensed:ital,wght@0,300;0,400;0,700;0,800;1,400&display=swap" rel="stylesheet">
<style>
  :root {
    --navy: #0b3f8f;
    --blue: #0455a3;
    --sky: #85cae6;
    --sky-pale: #dcf0f9;
    --grey: #aaaaaa;
    --ink: #222833;
    --white: #ffffff;
    --backdrop: #1b5b80;
  }
  * { box-sizing: border-box; margin: 0; padding: 0; }
  html, body { width: 1200px; height: 1200px; overflow: hidden; }
  body {
    background: var(--backdrop);
    font-family: "Roboto Condensed", sans-serif;
    position: relative;
  }
  .card {
    position: absolute;
    background: var(--white);
    width: 644px;
    height: 496px;
    overflow: hidden;
    box-shadow: 0 10px 24px rgba(0,0,0,0.35);
  }
  .card svg.decor { position: absolute; inset: 0; }

  /* back side */
  .card-back { left: 44px; top: 44px; }
  .stamp-box {
    position: absolute; left: 490px; top: 0; width: 154px; height: 154px;
    border-left: 1px solid #d6d6d6; border-bottom: 1px solid #d6d6d6;
  }
  .headline { position: absolute; left: 54px; top: 50px; color: var(--blue); }
  .headline .big { font-size: 46px; font-weight: 400; line-height: 1; display: block; }
  .headline .mid { font-size: 24px; font-weight: 400; line-height: 1.3; display: block; margin: 4px 0 0; }
  .headline .big + .mid + .big { margin-top: 2px; }
  .story {
    position: absolute; left: 55px; top: 196px; width: 232px;
    font-size: 10px; line-height: 12.4px; color: var(--white);
    text-align: justify; font-weight: 300;
  }
  .address-lines { position: absolute; left: 392px; top: 306px; width: 210px; }
  .address-lines span { display: block; height: 26px; border-top: 1px solid #333; }
  .back-footer { position: absolute; left: 56px; top: 392px; display: flex; align-items: center; }
  .brand { display: flex; align-items: center; gap: 5px; color: #7d8590; font-weight: 400; white-space: nowrap; }
  .brand .dot { width: 8px; height: 8px; border-radius: 50%; background: var(--sky); flex: none; }
  .back-footer .brand { font-size: 8.5px; letter-spacing: 0.4px; width: 78px; }
  .contact {
    border-left: 1px solid var(--ink); padding-left: 9px; margin-left: 4px;
    font-size: 10px; line-height: 13px; color: var(--ink); white-space: nowrap;
  }

  /* front side */
  .card-front { left: 412px; top: 600px; }
  .photo { position: absolute; }
  .photo-trainer { left: 0; top: 0; width: 180px; height: 286px; background: linear-gradient(160deg, #d9d6cf, #9a968e 70%, #5a5650); }
  .photo-before { left: 0; top: 290px; width: 85px; height: 206px; background: linear-gradient(180deg, #c9c1b1, #6b5a48 75%, #2a211b); }
  .photo-after { left: 89px; top: 290px; width: 91px; height: 206px; background: linear-gradient(180deg, #d4cfc6, #7d7468 75%, #2f2a26); }
  .photo-session { left: 186px; top: 0; width: 320px; height: 178px; background: linear-gradient(150deg, #cfcfcf, #7f8790 60%, #3a3f46); }
  .photo-device { left: 186px; top: 182px; width: 61px; height: 180px; background: linear-gradient(180deg, #4e8996, #2b3a40 70%, #1d2124); }
  .photo-client { left: 251px; top: 182px; width: 95px; height: 180px; background: linear-gradient(180deg, #8a5a50, #3a4b66 70%, #263040); }
  .photo-floor { left: 186px; top: 366px; width: 120px; height: 130px; background: linear-gradient(180deg, #b7b7b2, #3c4350 60%, #4c4f55); }

  .offer { position: absolute; right: 54px; top: 92px; text-align: right; }
  .offer .brand { justify-content: flex-end; font-size: 17px; letter-spacing: 1px; margin-bottom: 24px; }
  .offer .brand .dot { width: 14px; height: 14px; }
  .offer-free { color: var(--blue); font-size: 40px; font-weight: 700; line-height: 0.95; }
  .offer-consult { color: var(--sky); font-size: 31px; font-weight: 700; line-height: 1.05; }
  .offer-discount { color: var(--blue); font-size: 56px; font-weight: 800; line-height: 0.95; letter-spacing: -1px; }
  .offer-first { color: var(--sky); font-size: 24px; font-weight: 700; line-height: 1.2; }
  .tagline { color: var(--blue); font-size: 21px; font-style: italic; font-weight: 400; margin-top: 4px; }
  .pitch {
    width: 240px; margin: 4px 0 0 auto; text-align: justify; text-align-last: left;
    font-size: 11.5px; line-height: 15px; color: var(--ink);
  }
  .web { font-size: 11px; letter-spacing: 5.2px; color: var(--ink); margin-top: 8px; margin-right: -5px; }
</style>
</head>
<body>

<section class="card card-back" aria-label="Postcard back">
  <svg class="decor" width="644" height="496" viewBox="0 0 644 496" aria-hidden="true">
    <defs>
      <linearGradient id="backBand" x1="0" y1="0" x2="0" y2="1">
        <stop offset="0" stop-color="#ffffff"/>
        <stop offset="0.35" stop-color="#b9c3e0"/>
        <stop offset="1" stop-color="#1e4aa0"/>
      </linearGradient>
      <linearGradient id="backArc" x1="0" y1="1" x2="1" y2="0">
        <stop offset="0" stop-color="#0455a3"/>
        <stop offset="1" stop-color="#85cae6"/>
      </linearGradient>
    </defs>
    <path d="M0 88 H470 C420 170 370 270 355 386 H0 Z" fill="url(#backBand)"/>
    <path d="M348 496 C330 380 370 240 470 110 C390 250 360 380 372 496 Z" fill="url(#backArc)"/>
    <path d="M378 496 C380 380 430 240 540 90 C460 240 410 370 404 496 Z" fill="#85cae6" opacity="0.55"/>
    <path d="M420 496 C460 420 540 360 610 250 C580 360 500 440 460 496 Z" fill="#dcf0f9" opacity="0.8"/>
  </svg>
  <div class="stamp-box"></div>
  <h1 class="headline">
    <span class="big">Up To 18 Times</span>
    <span class="mid">More Effective Than A Conventional</span>
    <span class="big">Gym Workout</span>
  </h1>
  <p class="story">Marissa founded Cobalt Stride on the core belief that she should use her unique experiences and access to the best in wellness technologies to help other people achieve their fitness goals. Marissa joined a big 4 accounting firm after graduating from Ridgeview University, where she played collegiate Division 1 volleyball. Driven to excel in the fast-paced business world, and committed to maintain her elite athleticism, Marissa experienced what many of us feel in our day to day lives: there is always so much to do, that staying fit is a struggle. Then crisis struck. In the spring of 2012 Marissa began to feel extremely fatigued all day, every day and to gain weight at an unexpected pace. Marissa sought the help of doctors and specialists in Southern California, but her health continued to deteriorate.</p>
  <div class="address-lines" aria-hidden="true"><span></span><span></span><span></span><span></span></div>
  <footer class="back-footer">
    <div class="brand"><span class="dot"></span>COBALT STRIDE</div>
    <div class="contact">
      (949) 555-0137<br>
      cobaltstridehealth@mailbox.example<br>
      www.cobalt-stride.example<br>
      327 Venadero Ave, Building B Suite 518<br>
      Costa Mesa CA 92626
    </div>
  </footer>
</section>

<section class="card card-front" aria-label="Postcard front">
  <div class="photo photo-trainer" role="img" aria-label="Trainer posing with dumbbells in the studio"></div>
  <div class="photo photo-before" role="img" aria-label="Client before photo"></div>
  <div class="photo photo-after" role="img" aria-label="Client after photo"></div>
  <div class="photo photo-session" role="img" aria-label="Trainer and client during a session on the device"></div>
  <div class="photo photo-device" role="img" aria-label="Trainer beside the training device"></div>
  <div class="photo photo-client" role="img" aria-label="Client smiling in a training suit"></div>
  <div class="photo photo-floor" role="img" aria-label="Client exercising on the floor"></div>
  <svg class="decor" width="644" height="496" viewBox="0 0 644 496" aria-hidden="true">
    <defs>
      <linearGradient id="frontArc" x1="0" y1="1" x2="1" y2="0">
        <stop offset="0" stop-color="#0455a3"/>
        <stop offset="0.5" stop-color="#85cae6"/>
        <stop offset="1" stop-color="#dcf0f9"/>
      </linearGradient>
    </defs>
    <path d="M296 496 C296 330 386 140 506 0 H644 V496 Z" fill="#ffffff"/>
    <path d="M272 496 C272 330 362 140 482 0 H506 C386 140 296 330 296 496 Z" fill="url(#frontArc)"/>
    <path d="M400 496 C500 470 590 420 644 380 V420 C600 455 540 485 500 496 Z" fill="#85cae6" opacity="0.5"/>
    <path d="M520 496 C580 475 620 455 644 440 V496 Z" fill="#dcf0f9"/>
  </svg>
  <div class="offer">
    <div class="brand"><span class="dot"></span>COBALT STRIDE</div>
    <div class="offer-free">FREE</div>
    <div class="offer-consult">CONSULTATION</div>
    <div class="offer-discount">50% off</div>
    <div class="offer-first">YOUR FIRST SESSION</div>
    <div class="tagline">Lose Weight. Gain Muscle.</div>
    <p class="pitch">Customized Personal training using V-Core, the latest technology in fitness. Reach your fitness goals in just two 25-min sessions per week</p>
    <div class="web">www.cobalt-stride.example</div>
  </div>
</section>

</body>
</html>
```